Business card for Eyelash extension salon in Alder Glen,California USA

We need new business card for our salon in Alder Glen. The salon name is 'Lashvora' . We would like to have...Business name: Lashvora Name of person: will provide later Address 6812 N.Calder Ridge Ave Alder Glen , CA 90999 Phone: will provide later (Text only) Web: www.lashvorastudio-demo.com Instagram icon, Facebook icon follow us for seasonal campaign and news @lashvorastudiodemo Design should look elegant, high-end, clean, simple, cohesive with my brand. Please refer my brand board. Business name color will be metallic bronzy color. Im thinking grey background or white background. Thanks

Target Market(s)

25-35. Gender neutral. People who are in Entertainment business industry.
This is High-end Eyelash extension salon in Alder Glen

Industry/Entity Type

Beauty Salon

Contact Information for Business Card

Business name: Lashvora
Name of person: will provide later
Address 6812 N.Calder Ridge Ave Alder Glen , CA 90999
Phone: will provide later (Text only)
Web: www.lashvorastudio-demo.com
Instagram icon, Facebook icon
follow us for seasonal campaign and news @lashvorastudiodemo

Requirements
Must have
• Beautiful, elegant, clean and simple look but very attractive and modern
Should not have
• We don't like too clutter, too busy designs.

```html
<!DOCTYPE html>
<html lang="en">
<head>
<meta charset="utf-8">
<title>Lashvora – Business Card</title>
<link rel="stylesheet" href="https://fonts.googleapis.com/css2?family=Arimo:wght@700&family=Open+Sans:ital,wght@0,400;0,600;1,700&display=swap">
<style>
  :root {
    --backdrop: #ece8e3;
    --kraft-light: #dcbb92;
    --kraft-mid: #c79d6c;
    --kraft-dark: #b8895a;
    --ink: #111111;
    --rule: #6b5337;
  }
  * { margin: 0; padding: 0; box-sizing: border-box; }
  html, body {
    width: 1200px; height: 900px; overflow: hidden;
    background: var(--backdrop);
  }
  .canvas { position: relative; width: 1200px; height: 900px; }
  .card {
    position: absolute;
    background: radial-gradient(ellipse at 40% 0%, var(--kraft-light) 0%, var(--kraft-mid) 55%, var(--kraft-dark) 100%);
    box-shadow: 4px 6px 8px rgba(0,0,0,0.35);
    color: var(--ink);
    font-family: "Open Sans", sans-serif;
  }
  .card--contact { left: 329px; top: 90px; width: 556px; height: 343px; text-align: center; }
  .card--brand { left: 329px; top: 469px; width: 560px; height: 344px; }

  .contact__name {
    position: absolute; left: 0; right: 0; top: 96px;
    font-family: "Arimo", sans-serif; font-weight: 700; font-size: 19px; letter-spacing: 0.3px;
  }
  .contact__rule {
    position: absolute; left: 206px; width: 144px; height: 1px; background: var(--ink);
  }
  .contact__rule--top { top: 130px; }
  .contact__rule--bottom { top: 192px; }
  .contact__block {
    position: absolute; left: 0; right: 0; font-size: 15px; line-height: 20px;
  }
  .contact__block--reach { top: 139px; }
  .contact__block--address { top: 203px; }

  .brand__name {
    position: absolute; left: 0; right: 0; top: 82px; text-align: center;
    font-size: 80px; font-weight: 400; letter-spacing: 1px; line-height: 1;
  }
  .brand__place {
    position: absolute; left: 275px; top: 212px;
    font-size: 10px; letter-spacing: 2.4px;
  }
  .brand__social { position: absolute; left: 0; top: 258px; width: 560px; height: 26px; }
  .brand__follow {
    position: absolute; left: 0; right: 0; top: 292px; text-align: center; font-size: 15px;
  }
  .brand__handle { font-weight: 700; font-style: italic; }
</style>
</head>
<body>
<main class="canvas">
  <section class="card card--contact">
    <h1 class="contact__name">MARCUS ELLERY</h1>
    <div class="contact__rule contact__rule--top"></div>
    <p class="contact__block contact__block--reach">044-555 010 248<br>www.lashvorastudio-demo.com</p>
    <div class="contact__rule contact__rule--bottom"></div>
    <p class="contact__block contact__block--address">6812 N.Calder Ridge Ave<br>Alder Glen , CA 90999</p>
  </section>

  <section class="card card--brand">
    <h2 class="brand__name">Lashvora</h2>
    <p class="brand__place">ALDER GLEN</p>
    <svg class="brand__social" viewBox="0 0 560 26" aria-hidden="true">
      <line x1="58" y1="13" x2="262" y2="13" stroke="var(--rule)" stroke-width="0.8"/>
      <line x1="298" y1="13" x2="493" y2="13" stroke="var(--rule)" stroke-width="0.8"/>
      <circle cx="280" cy="13" r="12" fill="var(--ink)"/>
    </svg>
    <p class="brand__follow">Follow us for seasonal campaign and news <span class="brand__handle">@lashvorastudiodemo</span></p>
  </section>
</main>
</body>
</html>
```